Towing company card on one side and our Autobody and collision repair shop card on the other

We need a two sided business card on one side it would be for our towing company and the other for our auto body and collision repair shop we would like our logo to appear on the card on the autobody shop side .I would like the card to be unique not just a regular towing or auto body shop company card. Our tow truck company offers flatbed and wheel lift service short and long distance we also offer roadside assistance which covers jumpstarts, tire changes, lock outs we are on call 24/7. All of our trucks are state of the art and brand new with air ride suspension and low profile beds. The phone number for the towing company is 201-574-3902. We accept all major credit cards. The other side of the card would be for the Auto body shop specializing in auto painting, body and fender repair, frame straightening , unibody repair and fiberglass repair work. We color match factory paint and we handle all insurance companies claims.The phone number for the auto body shop is 201-368-2915 fax 201-368-2915 email redfinchautobody@mailvale.net the autobody license number must appear on the autobody side of the card in this format. LIC#04817C

Target Market(s)

new customers

Industry/Entity Type

Business

Contact Information for Business Card

towing company on one side and auto body and collision repair on the other side

Colors
ec1f27
000000
aaaaaa
e9e9e9
0555a3
959595
1b1b1b

Requirements
Must have
• Must have company logo on card on the autobody side of card and show address 4816 Garvick ave Eastwood NJ 07391

```html
<!DOCTYPE html>
<html lang="en">
<head>
<meta charset="utf-8">
<title>Red Finch Autobody – Business Card</title>
<link href="https://fonts.googleapis.com/css2?family=Open+Sans:wght@400;700;800&family=Rajdhani:wght@700&display=swap" rel="stylesheet">
<style>
  :root {
    --brand-red: #ec1f27;
    --ink: #1b1b1b;
    --card: #e9e9e9;
    --backdrop: #c9c9c9;
    --band-text: #f6c9cb;
  }
  * { margin: 0; padding: 0; box-sizing: border-box; }
  html, body { width: 1200px; height: 1054px; overflow: hidden; }
  body {
    background: var(--backdrop);
    font-family: "Open Sans", Arial, sans-serif;
    position: relative;
  }
  .business-card {
    position: absolute;
    left: 100px; top: 226px;
    width: 1000px; height: 602px;
    background: var(--card);
    border: 1px solid #f4f4f4;
    box-shadow: 0 4px 18px rgba(0,0,0,0.12);
    overflow: hidden;
  }
  .license {
    position: absolute;
    left: 63px; top: 96px;
    font-family: "Rajdhani", "Arial Narrow", sans-serif;
    font-weight: 700;
    font-size: 34px;
    letter-spacing: 0.5px;
    color: var(--brand-red);
  }
  .contact-list { position: absolute; left: 63px; top: 164px; list-style: none; }
  .contact-item {
    display: flex; align-items: flex-start;
    font-size: 25px; line-height: 40px; color: var(--ink);
  }
  .contact-icon { width: 24px; height: 40px; margin-right: 22px; flex: none; }
  .contact-icon svg { display: block; margin-top: 9px; }
  .service-band {
    position: absolute;
    left: 0; top: 452px;
    width: 724px; height: 99px;
    background: var(--brand-red);
    clip-path: polygon(0 0, 100% 0, 97.5% 100%, 0 100%);
    padding: 14px 0 0 63px;
  }
  .service-line {
    font-size: 22px; line-height: 36px;
    color: var(--band-text); white-space: nowrap;
  }
  .service-line .sep { margin: 0 10px; }
  .brand-mark {
    position: absolute;
    left: 800px; top: 40px;
    width: 140px; height: 522px;
    display: flex; flex-direction: column; align-items: center; justify-content: center; gap: 18px;
  }
  .brand-name {
    writing-mode: vertical-rl;
    transform: rotate(180deg);
    font-weight: 800;
    font-size: 52px;
    letter-spacing: 1px;
    color: var(--ink);
    white-space: nowrap;
  }
  .brand-dot { width: 26px; height: 26px; border-radius: 50%; background: var(--brand-red); }
</style>
</head>
<body>
  <section class="business-card" aria-label="Red Finch Autobody business card">
    <div class="license">LIC#04817C</div>

    <ul class="contact-list">
      <li class="contact-item">
        <span class="contact-icon"><svg width="24" height="22" viewBox="0 0 24 22"><path fill="#ec1f27" d="M2 7c0-3 4-5 10-5s10 2 10 5v2h-5V7c-1-1-3-1.5-5-1.5S8 6 7 7v2H2zM6 10l2-3h8l2 3 3 3v7H3v-7zm6 1a3 3 0 1 0 0 6 3 3 0 0 0 0-6z"/></svg></span>
        <span>201-368-2915</span>
      </li>
      <li class="contact-item">
        <span class="contact-icon"><svg width="24" height="18" viewBox="0 0 24 18"><path fill="#ec1f27" d="M1 1h22v16H1zM3 3v1l9 7 9-7V3l-9 6z"/></svg></span>
        <span>redfinchautobody@mailvale.net</span>
      </li>
      <li class="contact-item">
        <span class="contact-icon"><svg width="20" height="26" viewBox="0 0 20 26"><path fill="#ec1f27" d="M10 0a9 9 0 0 0-9 9c0 7 9 17 9 17s9-10 9-17a9 9 0 0 0-9-9zm0 5a4 4 0 1 1 0 8 4 4 0 0 1 0-8z"/></svg></span>
        <span>4816 Garvick AVE<br>Eastwood NJ 07391</span>
      </li>
    </ul>

    <div class="service-band">
      <p class="service-line">Auto Painting<span class="sep">•</span>Unibody Repair<span class="sep">•</span>Frame Straightening</p>
      <p class="service-line">Body &amp; Fender Repair<span class="sep">•</span>Fiberglass Repair Work</p>
    </div>

    <div class="brand-mark">
      <span class="brand-name">Red Finch Autobody</span>
      <span class="brand-dot" aria-hidden="true"></span>
    </div>
  </section>
</body>
</html>
```